Presentation and Communication Coaching Services Business needs updated interactive web site

I want to keep the color scheme, functionality, and pages of my current site, but with a newer/updated look. I need to improve security and simplify images, etc. (Please see current site http://brackleyvoicementor.com ) This will need be functional on mobile devices, as well.

I'm attached to the scrolling client list and scrolling client feedback.

Industry/Entity Type

Professional Service

Font styles to use
Sans Serif

Colors
0356a4
f37122
33a6d7

Requirements
Must have
• scrolling client banner on home page, client comments slider, color scheme
• Please see current site: http://brackleyvoicementor.com
Nice to have
• better action/appearance
Should not have
• I don't want it to look like all the other sites/templates

```html
<!DOCTYPE html>
<html lang="en">
<head>
<meta charset="utf-8">
<title>Services We Provide – Brackley Voice Mentor</title>
<link href="https://fonts.googleapis.com/css2?family=Questrial&display=swap" rel="stylesheet">
<style>
:root{
  --bg-top:#0c3246;
  --bg-mid:#123f55;
  --bg-low:#1a5068;
  --bar:#143647;
  --gold:#eeaa2c;
  --teal:#3c93b3;
  --teal-soft:#5aa9c6;
  --tab:#2f5b6d;
  --tab-edge:#e2a93a;
  --ink:#2b4b5c;
  --white:#ffffff;
  --muted:#b7cbd5;
}
*{margin:0;padding:0;box-sizing:border-box}
html,body{width:1034px;height:1200px;overflow:hidden}
body{font-family:"Questrial",sans-serif;color:var(--white);
  background:linear-gradient(180deg,var(--bg-top) 0%,var(--bg-mid) 45%,var(--bg-low) 85%,var(--bg-mid) 100%)}
.page{position:relative;width:1034px;height:1200px;overflow:hidden}
.abs{position:absolute}

.brand{left:129px;top:19px;font-size:20px;letter-spacing:.2px;color:var(--white)}

.social{display:flex;gap:10px}
.social span{width:26px;height:26px;border-radius:50%;border:1px solid #4f7d90;display:block}
.social span.on{background:var(--teal);border-color:var(--teal)}
.header-social{left:485px;top:17px}

.btn{display:flex;align-items:center;justify-content:center;border-radius:14px;font-size:11px;height:27px}
.btn-gold{background:var(--gold);color:var(--white)}
.btn-teal{background:var(--teal);color:var(--white)}
.register{left:659px;top:18px;width:117px}
.login{left:788px;top:18px;width:117px;gap:6px}

.nav{top:71px;left:0;width:100%;font-size:10.5px;letter-spacing:1px}
.nav a{position:absolute;color:var(--white);text-decoration:none}
.nav a.current{color:var(--teal-soft)}

.hero-art{left:325px;top:158px;width:165px;height:165px;border-radius:50%;
  background:radial-gradient(circle at 45% 40%,#3d8098 0%,#1d5168 55%,rgba(18,63,85,0) 72%);opacity:.85}
.hero-title{left:0;top:218px;width:1034px;text-align:center;color:var(--gold);font-size:25px;font-weight:400}

.photo{left:323px;top:362px;width:582px;height:258px;
  background:linear-gradient(120deg,#9fd0e6 0%,#d8eef7 40%,#c7dce6 70%,#7fa9bd 100%)}

.tabs{left:129px;top:394px;width:194px;z-index:2}
.tab{position:absolute;left:0;width:194px;height:39px;background:var(--tab);border-left:3px solid var(--tab-edge);
  font-size:13px;padding-left:16px;display:flex;align-items:center;color:var(--white)}
.tab.active{background:var(--white);color:var(--gold)}
.tab.active::after{content:"";position:absolute;right:-18px;top:0;border-left:18px solid var(--white);
  border-top:19.5px solid transparent;border-bottom:19.5px solid transparent}

.panel{left:323px;top:620px;width:582px;height:330px;background:var(--white);padding:28px 34px 28px 32px;color:var(--ink)}
.panel .lead{font-size:11px;margin-bottom:13px}
.panel h3{font-weight:400;color:var(--gold);font-size:13px;margin:0 0 6px}
.panel p{font-size:11px;line-height:15.5px;letter-spacing:.15px;margin-bottom:13px}

.owner{left:129px;top:1010px;color:var(--gold);font-size:25px}
.role{left:129px;top:1041px;font-size:12px}
.about{left:129px;top:1073px;width:360px;font-size:10.5px;line-height:15.5px;color:var(--muted)}
.contact-btn{left:549px;top:1016px;width:117px}
.contact-line{left:549px;top:1061px;font-size:12px;letter-spacing:.3px}
.contact-line .sep{margin:0 12px}
.footer-social{left:549px;top:1094px}
.footer-register{left:724px;top:1094px;width:116px}
.to-top{left:958px;top:1014px}

.bottom-bar{left:0;top:1161px;width:1034px;height:39px;background:var(--bar);font-size:10px;color:var(--muted)}
.bottom-bar .copy{position:absolute;left:129px;top:14px}
.bottom-bar .links{position:absolute;right:129px;top:14px}
.bottom-bar .links .sep{margin:0 14px}
</style>
</head>
<body>
<div class="page">
  <div class="abs brand">Brackley Voice Mentor</div>
  <div class="abs social header-social" aria-label="Social links">
    <span></span><span class="on"></span><span></span><span></span><span></span>
  </div>
  <div class="abs btn btn-gold register">Register Now!</div>
  <div class="abs btn btn-teal login">
    <svg width="10" height="11" viewBox="0 0 10 11" fill="none" stroke="#fff" stroke-width="1.2"><circle cx="5" cy="3.2" r="2.4"/><path d="M1 10.5c0-2.5 1.8-4 4-4s4 1.5 4 4"/></svg>
    Client Login
  </div>
  <nav class="abs nav">
    <a style="left:133px">HOME</a>
    <a style="left:231px">ABOUT</a>
    <a style="left:337px">CLIENTS</a>
    <a style="left:448px">REVIEWS</a>
    <a class="current" style="left:563px">SERVICES</a>
    <a style="left:682px">CONTACT</a>
    <a style="left:803px">SPEAKING SECRETS</a>
  </nav>

  <div class="abs hero-art" role="img" aria-label="Close-up of a studio microphone"></div>
  <h1 class="abs hero-title">Services We Provide</h1>

  <div class="abs photo" role="img" aria-label="Business colleagues working together at a bright office desk"></div>

  <div class="abs tabs">
    <div class="tab" style="top:0">Coaching</div>
    <div class="tab active" style="top:52px">Accents</div>
    <div class="tab" style="top:104px">Custom Workshops</div>
    <div class="tab" style="top:155px">Keynote Speeches</div>
  </div>

  <div class="abs panel">
    <p class="lead">Individual Accent Modification Coaching to Maximize Intelligibility and Diminish Confusion</p>
    <h3>The Challenge:</h3>
    <p>Many speaking English as a second or third language have never been given direct, one-on-one feedback for challenging sounds and stress patterns that exist in English and nowhere else. They are doomed to being misunderstood and potentially disregarded due to simple issues of pronunciation and style, despite their competence and expertise.</p>
    <h3>The Method:</h3>
    <p>Knowledge and use of the phonetic alphabet and the physiology and mechanics of sound production come together in one-on-one sessions including interactive work, exercises and audio materials. Customized "homework" complements the work done in session.</p>
    <h3>The Result:</h3>
    <p>New awareness and a change in habits allowing the expertise and personality of the client to shine through, improving communication at work and elsewhere.</p>
  </div>

  <div class="abs owner">Helena Brackley</div>
  <div class="abs role">Public Speaking Consultant</div>
  <p class="abs about">Providing highly specialized executive coaching services and program design and facilitation for leadership development, public speaking, and all areas of spoken communication.</p>
  <div class="abs btn btn-teal contact-btn">Contact Us</div>
  <div class="abs contact-line">e. info@brackleyvoicementor.com<span class="sep">|</span>p. 555.014.2290</div>
  <div class="abs social footer-social" aria-label="Social links">
    <span></span><span class="on"></span><span></span><span></span><span></span>
  </div>
  <div class="abs btn btn-gold footer-register">Register Now!</div>
  <svg class="abs to-top" width="22" height="24" viewBox="0 0 22 24" fill="none" stroke="#fff" stroke-width="2" aria-label="Back to top"><path d="M2 22L11 2l9 20M6 14h10"/></svg>

  <footer class="abs bottom-bar">
    <span class="copy">© 2019 Brackley Voice Mentor.</span>
    <span class="links">Privacy Policy<span class="sep">|</span>Sitemap</span>
  </footer>
</div>
</body>
</html>
```